Business Card Colourful and fun Design Project

I need a business card design for my Ecommerce website which am launching soon. we are based in the United Arab Emirates and our customers are based in Dubai and other cities in UAE, In addition to our neighbour countries in the GCC. We sell Gadgets, fashion and other trendy stuff that are hard to find in our market. The company name is "ZIPKOALA" logo consists of a panda wearing traditional local Arab thobe. would like to see a clean, colourful fun design to represent us.
Updates
please read the discussion board. thanks
Industry/Entity Type
Fashion
Look and feel
Each slider illustrates characteristics of the customer's brand and the style your logo design should communicate.

```html
<!DOCTYPE html>
<html lang="en">
<head>
<meta charset="utf-8">
<title>ZIPKOALA Business Card</title>
<link rel="stylesheet" href="https://fonts.googleapis.com/css2?family=Barlow+Semi+Condensed:wght@400;500;600;700&display=swap">
<style>
  :root {
    --backdrop: #383b34;
    --brand-red: #c1272d;
    --card-grey: #cdcdcd;
    --ink: #1c1c1c;
    --wordmark: #333333;
    --social-ink: #f3e6e6;
    --mascot-tone: #e9e6e2;
  }
  * { margin: 0; padding: 0; box-sizing: border-box; }
  html, body {
    width: 1200px; height: 959px; overflow: hidden;
    background: var(--backdrop);
    font-family: "Barlow Semi Condensed", "Arial Narrow", sans-serif;
  }
  .canvas { position: relative; width: 1200px; height: 959px; }
  .card {
    position: absolute; width: 490px; height: 320px;
    border-radius: 10px; overflow: hidden; background: var(--card-grey);
  }
  .card-front { left: 378px; top: 130px; }
  .card-back { left: 383px; top: 503px; }
  .card-shape { position: absolute; inset: 0; }
  .card-shape .red-panel { fill: var(--brand-red); }
  .mascot-spot {
    position: absolute; left: 42px; top: 60px; width: 110px; height: 110px;
    border-radius: 50%; background: var(--mascot-tone);
  }
  .wordmark {
    position: absolute; left: 150px; top: 124px;
    font-size: 64px; font-weight: 500; line-height: 1;
    color: var(--wordmark); letter-spacing: 1px;
  }
  .tagline {
    position: absolute; left: 170px; top: 208px;
    font-size: 17px; font-weight: 600; color: var(--ink);
  }
  .contact {
    position: absolute; left: 326px; top: 9px;
    font-size: 15px; line-height: 22px; color: var(--ink);
  }
  .contact .email { font-weight: 700; }
  .holder-name {
    position: absolute; left: 196px; top: 118px;
    font-size: 41px; font-weight: 700; line-height: 1; color: #000;
  }
  .holder-role {
    position: absolute; left: 210px; top: 160px;
    font-size: 15px; color: var(--ink);
  }
  .social {
    position: absolute; left: 14px; top: 234px;
    list-style: none; font-size: 17px; line-height: 24px; color: var(--social-ink);
  }
</style>
</head>
<body>
<main class="canvas">
  <section class="card card-front">
    <svg class="card-shape" viewBox="0 0 490 320" preserveAspectRatio="none">
      <path class="red-panel" d="M0 0 H242 C262 40 290 90 262 170 C238 240 230 280 247 320 H0 Z"/>
    </svg>
    <div class="mascot-spot" aria-hidden="true"></div>
    <div class="wordmark">zipkoala</div>
    <p class="tagline">Found nowhere, we’ll give you.</p>
  </section>

  <section class="card card-back">
    <svg class="card-shape" viewBox="0 0 490 320" preserveAspectRatio="none">
      <path class="red-panel" d="M0 0 H245 C265 40 290 100 262 170 C238 230 225 280 245 320 H0 Z"/>
    </svg>
    <div class="contact">
      <p class="phone">Phone:</p>
      <p class="email">Email:</p>
    </div>
    <h1 class="holder-name">NAME</h1>
    <p class="holder-role">Designation</p>
    <ul class="social">
      <li>facebook.com/zipkoalauae</li>
      <li>@zipkoalauae</li>
      <li>instagram:zipkoalauae</li>
    </ul>
  </section>
</main>
</body>
</html>
```